Quarnfield Fintech Product Infographic

Quarnfield is an established Fintech business, supplying complex financial software to banks and building societies.

We currently have a picture/infographic to show each of our 11 different software products in a single image. Each product can be installed on its own as a standalone application or if multiple products are installed they will share data.

The key message for our infographic is to convey the integration via a shared database.

The attached diagram is what we currently use which is to give you an idea of the message we are trying to give, but we are not tied to this format and are looking for this diagram to be reimagined.

We will look to use our new chosen design on printed media such as A4 Data sheets an example of which is attached.

For more information on our products please refer to www.quarnfield-example.co.uk/products

```html
<!DOCTYPE html>
<html lang="en">
<head>
<meta charset="utf-8">
<title>Quarnfield Fintech Product Infographic</title>
<link href="https://fonts.googleapis.com/css2?family=Poppins:wght@500;600;700&display=swap" rel="stylesheet">
<style>
  :root {
    --ink: #111111;
    --white: #ffffff;
    --performance: #D07ACD;
    --performance-ring: #BE6BBB;
    --performance-label: #7A2E77;
    --finance: #00A8E1;
    --finance-ring: #0095CB;
    --finance-label: #0D5C85;
    --risk: #FCBD53;
    --risk-ring: #E5A849;
    --risk-label: #9A6412;
    --regulatory: #45DC96;
    --regulatory-ring: #3CC386;
    --regulatory-label: #177146;
    --shared: #4E6493;
  }
  * { margin: 0; padding: 0; box-sizing: border-box; }
  html, body { width: 1200px; height: 901px; overflow: hidden; background: var(--white); }
  body { font-family: "Poppins", sans-serif; }
  .canvas { position: relative; width: 1200px; height: 901px; }
  .title {
    position: absolute; left: 0; width: 1210px; text-align: center;
    font-weight: 700; font-size: 29px; color: var(--ink); line-height: 1;
  }
  .title--top { top: 42px; }
  .title--bottom { top: 95px; }
  .title-rule { position: absolute; left: 316px; top: 82px; width: 578px; height: 4px; display: flex; }
  .title-rule span { flex: 1; }
  .diagram { position: absolute; left: 0; top: 0; }
  .feature-list { position: absolute; list-style: none; color: var(--white); font-weight: 500; font-size: 17.5px; line-height: 36.5px; }
  .feature-list li { position: relative; padding-left: 26px; }
  .feature-list li::before {
    content: ""; position: absolute; left: 0; top: 15px; width: 7px; height: 7px;
    border-radius: 50%; background: var(--white);
  }
  .list--performance { left: 285px; top: 207px; }
  .list--finance { left: 688px; top: 207px; }
  .list--risk { left: 285px; top: 705px; }
  .list--regulatory { left: 688px; top: 705px; }
  .area-label { position: absolute; font-weight: 600; font-size: 21px; letter-spacing: 1px; line-height: 1; }
  .label--performance { left: 283px; top: 359px; color: var(--performance-label); }
  .label--finance { left: 797px; top: 359px; color: var(--finance-label); }
  .label--risk { left: 343px; top: 641px; color: var(--risk-label); }
  .label--regulatory { left: 771px; top: 641px; color: var(--regulatory-label); }
  .shared-label {
    position: absolute; left: 505px; width: 200px; top: 563px; text-align: center;
    font-weight: 600; font-size: 21px; letter-spacing: 1px; color: var(--shared); line-height: 1;
  }
</style>
</head>
<body>
<main class="canvas">
  <h1 class="title title--top">QUARNFIELD FINTECH PRODUCT</h1>
  <div class="title-rule">
    <span style="background:var(--performance)"></span>
    <span style="background:var(--finance)"></span>
    <span style="background:var(--regulatory)"></span>
    <span style="background:var(--risk)"></span>
  </div>
  <h2 class="title title--bottom">INFOGRAPHIC</h2>

  <svg class="diagram" width="1200" height="901" viewBox="0 0 1200 901" aria-hidden="true">
    <defs>
      <clipPath id="clip-performance"><path d="M284 162 H585 V491 H256 V190 A28 28 0 0 1 284 162 Z"/></clipPath>
      <clipPath id="clip-finance"><path d="M626 162 H926 A28 28 0 0 1 954 190 V491 H626 Z"/></clipPath>
      <clipPath id="clip-risk"><path d="M256 530 H585 V859 H284 A28 28 0 0 1 256 831 Z"/></clipPath>
      <clipPath id="clip-regulatory"><path d="M626 530 H954 V831 A28 28 0 0 1 926 859 H626 Z"/></clipPath>
    </defs>

    <g clip-path="url(#clip-performance)">
      <rect x="256" y="162" width="329" height="329" fill="var(--performance)"/>
      <circle cx="605" cy="510" r="176" fill="var(--performance-ring)"/>
    </g>
    <g clip-path="url(#clip-finance)">
      <rect x="626" y="162" width="328" height="329" fill="var(--finance)"/>
      <circle cx="605" cy="510" r="176" fill="var(--finance-ring)"/>
    </g>
    <g clip-path="url(#clip-risk)">
      <rect x="256" y="530" width="329" height="329" fill="var(--risk)"/>
      <circle cx="605" cy="510" r="176" fill="var(--risk-ring)"/>
    </g>
    <g clip-path="url(#clip-regulatory)">
      <rect x="626" y="530" width="328" height="329" fill="var(--regulatory)"/>
      <circle cx="605" cy="510" r="176" fill="var(--regulatory-ring)"/>
    </g>

    <circle cx="605" cy="510" r="159" fill="var(--white)"/>

    <g class="connectors" fill="none" stroke="var(--white)" stroke-width="2.2" stroke-dasharray="4 4">
      <polyline points="363,403 397,460 446,460"/>
      <polyline points="848,403 822,460 764,460"/>
      <polyline points="363,616 404,560 447,560"/>
      <polyline points="848,616 809,560 764,560"/>
    </g>
    <g class="connector-ends" fill="none" stroke="var(--white)" stroke-width="2.2">
      <circle cx="361" cy="399" r="5"/>
      <circle cx="850" cy="399" r="5"/>
      <circle cx="361" cy="620" r="5"/>
      <circle cx="850" cy="620" r="5"/>
    </g>

    <g class="shared-icon">
      <path d="M536 430 a4 4 0 0 1 4 -4 H592 L600 439 H671 a4 4 0 0 1 4 4 V531 a4 4 0 0 1 -4 4 H540 a4 4 0 0 1 -4 -4 Z" fill="var(--shared)"/>
      <rect x="601" y="431" width="66" height="4" fill="var(--shared)"/>
      <g stroke="var(--white)" stroke-width="4">
        <line x1="593" y1="491" x2="618" y2="472"/>
        <line x1="593" y1="491" x2="618" y2="506"/>
      </g>
      <g fill="var(--white)">
        <circle cx="593" cy="491" r="10"/>
        <circle cx="619" cy="471" r="7.5"/>
        <circle cx="619" cy="506" r="7.5"/>
      </g>
    </g>
  </svg>

  <ul class="feature-list list--performance">
    <li>Financial Planning</li>
    <li>Funds Transfer Pricing</li>
    <li>Business Intelligence</li>
  </ul>
  <ul class="feature-list list--finance">
    <li>Financial Ledgers</li>
    <li>Effective Interest Rates</li>
    <li>Hedge Accounting</li>
  </ul>
  <ul class="feature-list list--risk">
    <li>Treasury</li>
    <li>ALM</li>
  </ul>
  <ul class="feature-list list--regulatory">
    <li>Regulatory Reporting</li>
    <li>Taxation Reporting</li>
    <li>FSCS SCV</li>
  </ul>

  <div class="area-label label--performance">PERFORMANCE</div>
  <div class="area-label label--finance">FINANCE</div>
  <div class="area-label label--risk">RISK</div>
  <div class="area-label label--regulatory">REGULATORY</div>
  <div class="shared-label">SHARED DATA</div>
</main>
</body>
</html>
```